Buch-/eBook-Cover für Anbieter von Seminaren zu den Themen Deeskalation und Selbstschutz
Zielgruppe
Ich gebe mit KLW Seminare (KLW steht für Kraft Lebt Weiter) Seminare, überwiegend bei Behörden, Firmen, Institutionen und Rettungskräfte zu den Themen Deeskalation und Selbstschutz. Darüber hinaus gebe ich auch Vorträge zum o.g. Thema und biete Selbstverteidigungskurse u.a. für Frauen an. Zielgruppe des Buches sind grundsätzlich alle Menschen die sich unsicher fühlen. Nicht für Kinder, aber ab dem jugendlichen Alter aufwärts. Dieses Buchprojekt ist bereits mein zweites. Es gibt bereits ein Buch zu dem Thema, wobei das aktuelle Buchprojekt etwas 'tiefer' in die Materie geht. Das erste Buch heißt: Wanderer im offenen Gelände - Das Handbuch für gelassenes Auftreten in Streitmomenten www.klw-seminare.de
Aufgabenstellung
Das Farbkonzept von KLW (blau, orange, weiß) sollte erkennbar sein. (Wiedererkennung). Endformat des Buchs 12,5 x 19,0 cm, Umschlag: Softcover 4/4-farbig. https://www.papierwerk-blatt.de wird die Druckerei sein.
Buchtitel: Ruhe wohnt in dir selbst - Wie du Linien ziehst, Streit entschärfst und dich wappnest
Ich benötige nach dem Design die Daten, um sie an die Druckerei weiterzugeben. Geplant ist davon auch ein ebook. Ich benötige für den Druck den Buchdeckel vorne/hinten sowie Buchrücken und Strichcode mit ISBN-Nummer (wird gesondert übersandt) auf der Rückseite.
Das Design darf nicht zu überladen sein.

```html
<!DOCTYPE html>
<html lang="de">
<head>
<meta charset="UTF-8">
<title>Ruhe wohnt in dir selbst – Buchcover</title>
<link rel="stylesheet" href="https://fonts.googleapis.com/css2?family=Inter:wght@300;400;800&display=swap">
<style>
  :root {
    --bg: #f4f4f4;
    --paper: #f7f5f2;
    --orange: #f5a11c;
    --blue: #2b6fcb;
    --blue-deep: #0f3d86;
    --blue-mid: #2a74d0;
    --blue-light: #7fb1ea;
    --white: #ffffff;
  }
  * { margin: 0; padding: 0; box-sizing: border-box; }
  html, body {
    width: 1199px; height: 1200px; overflow: hidden;
    background: var(--bg);
    font-family: "Inter", sans-serif;
  }
  .canvas {
    width: 1199px; height: 1200px;
    display: flex; align-items: center; justify-content: center;
  }
  .cover {
    position: relative;
    width: 716px; height: 1088px;
    background: var(--paper);
    overflow: hidden;
    text-align: center;
  }
  .author {
    position: absolute; top: 48px; left: 0; right: 0;
    font-weight: 400; font-size: 25px; letter-spacing: 0.32em;
    color: var(--blue);
  }
  .title { position: absolute; top: 118px; left: 0; right: 0; color: var(--orange); }
  .title-lead {
    display: block; font-weight: 300; font-size: 40px; letter-spacing: -0.02em; line-height: 1.1;
  }
  .title-main {
    display: block; font-weight: 800; font-size: 76px; line-height: 0.98; letter-spacing: -0.01em;
    margin-top: 6px;
  }
  .subtitle {
    position: absolute; top: 340px; left: 40px; right: 40px;
    font-weight: 300; font-size: 28px; line-height: 1.25; letter-spacing: -0.02em;
    color: var(--blue);
  }
  .scene {
    position: absolute; left: 0; top: 430px; width: 716px; height: 610px;
  }
  .brand {
    position: absolute; left: 0; right: 0; top: 910px;
    display: flex; flex-direction: column; align-items: center; color: var(--white);
  }
  .brand-row { display: flex; align-items: center; gap: 10px; }
  .brand-dot {
    width: 18px; height: 18px; border-radius: 50%;
    border: 2px solid var(--white);
  }
  .brand-name { font-weight: 400; font-size: 40px; letter-spacing: 0.18em; }
  .brand-claim { font-weight: 400; font-size: 15px; margin-top: 4px; }
</style>
</head>
<body>
<main class="canvas">
  <article class="cover">
    <p class="author">HENRIK STAHL</p>
    <h1 class="title">
      <span class="title-lead">RUHE WOHNT IN</span>
      <span class="title-main">DIR<br>SELBST</span>
    </h1>
    <p class="subtitle">Wie du Linien ziehst, Streit entschärfst<br>und dich wappnest</p>

    <svg class="scene" viewBox="0 0 716 610" role="img"
         aria-label="Blaue Doppelbelichtung: Profil-Silhouette eines Kopfes mit Bäumen und Stadtlichtern, davor eine kleine stehende Person, die hinaufblickt">
      <defs>
        <linearGradient id="sceneTone" x1="0" y1="0" x2="1" y2="1">
          <stop offset="0" stop-color="var(--blue-mid)"/>
          <stop offset="0.45" stop-color="var(--blue-deep)"/>
          <stop offset="1" stop-color="var(--blue-light)"/>
        </linearGradient>
      </defs>
      <path fill="url(#sceneTone)"
            d="M0 30 L40 22 L80 34 L120 18 L170 28 L215 8 L260 20 L300 4 L350 16 L400 10 L450 24 L500 14 L550 26 L600 12 L650 20 L690 6 L716 14
               L716 588 L690 596 L650 584 L610 598 L560 588 L520 600 L480 570 L440 560 L400 580 L360 592 L320 584 L280 600 L230 590 L180 602 L130 590 L80 600 L40 592 L0 600 Z"/>
    </svg>

    <div class="brand">
      <div class="brand-row">
        <span class="brand-dot"></span>
        <span class="brand-name">KLW</span>
      </div>
      <span class="brand-claim">Kraft Lebt Weiter</span>
    </div>
  </article>
</main>
</body>
</html>
```